Cedarbrook Lane Allies Stationery

Use attached logo for stationery
Stationery, Letterhead and Envelope + Business cards

Tag line: Walking alongside those doing the work of the Gospel

```html
<!DOCTYPE html>
<html lang="en">
<head>
<meta charset="utf-8">
<title>Cedarbrook Lane Allies – Business Card</title>
<link rel="stylesheet" href="https://fonts.googleapis.com/css2?family=Open+Sans:wght@400;600;700&display=swap">
<style>
  :root {
    --canvas-bg: #e4e6ea;
    --navy: #0a4a87;
    --navy-deep: #073e74;
    --card-white: #f4f4f4;
    --ink: #1f2a36;
    --name-blue: #0b4682;
    --sky: #4fc3e8;
  }
  * { box-sizing: border-box; margin: 0; padding: 0; }
  html, body {
    width: 1200px; height: 900px; overflow: hidden;
    background: var(--canvas-bg);
    font-family: "Open Sans", Arial, sans-serif;
  }
  .canvas {
    position: relative; width: 1200px; height: 900px;
  }
  .card {
    position: absolute; left: 250px; width: 700px; height: 400px;
    border-radius: 4px;
    box-shadow: 0 8px 22px rgba(0,0,0,0.18);
  }
  .card--front {
    top: 40px;
    background: radial-gradient(ellipse at 45% 35%, #0c5596 0%, var(--navy) 45%, var(--navy-deep) 100%);
    display: flex; align-items: center; justify-content: center;
  }
  .card--back {
    top: 470px;
    background: linear-gradient(160deg, #e9e9e9 0%, var(--card-white) 50%, #ececec 100%);
  }
  .brand {
    display: flex; align-items: center; gap: 12px;
    font-weight: 600; letter-spacing: 0.5px;
  }
  .brand__dot {
    width: 18px; height: 18px; border-radius: 50%;
    background: var(--sky);
    flex: none;
  }
  .card--front .brand { color: #ffffff; font-size: 30px; }
  .card--back .brand {
    position: absolute; left: 70px; top: 170px;
    color: var(--navy); font-size: 26px;
    width: 300px; line-height: 1.2;
  }
  .contact {
    position: absolute; left: 420px; top: 90px;
    color: var(--ink);
  }
  .contact__name {
    font-size: 26px; font-weight: 700; color: var(--name-blue); line-height: 1.1;
  }
  .contact__role { font-size: 18px; margin-top: 2px; }
  .contact__address { font-size: 18px; line-height: 1.45; margin-top: 22px; }
  .contact__list { list-style: none; margin-top: 20px; font-size: 18px; line-height: 1.6; }
  .contact__list li { display: flex; align-items: center; gap: 12px; }
  .contact__list svg { width: 18px; height: 18px; flex: none; }
</style>
</head>
<body>
<main class="canvas">
  <section class="card card--front" aria-label="Card front">
    <div class="brand"><span class="brand__dot"></span><span>Cedarbrook Lane Allies</span></div>
  </section>

  <section class="card card--back" aria-label="Card back">
    <div class="brand"><span class="brand__dot"></span><span>Cedarbrook Lane Allies</span></div>

    <div class="contact">
      <p class="contact__name">John Smith</p>
      <p class="contact__role">Manager</p>
      <p class="contact__address">99th Street, Exact Road<br>New cross side, CA 456982.</p>
      <ul class="contact__list">
        <li>
          <svg viewBox="0 0 24 24" aria-hidden="true"><path fill="var(--sky)" d="M6.6 10.8a15 15 0 0 0 6.6 6.6l2.2-2.2c.3-.3.7-.4 1-.2 1.1.4 2.3.6 3.6.6.6 0 1 .4 1 1V20c0 .6-.4 1-1 1A17 17 0 0 1 3 4c0-.6.4-1 1-1h3.5c.6 0 1 .4 1 1 0 1.3.2 2.5.6 3.6.1.3 0 .7-.2 1z"/></svg>
          <span>+999 9999 9999</span>
        </li>
        <li>
          <svg viewBox="0 0 24 24" aria-hidden="true"><rect x="2" y="5" width="20" height="14" rx="2" fill="var(--sky)"/><path d="M3 6l9 7 9-7" fill="none" stroke="#fff" stroke-width="1.8"/></svg>
          <span>info@mywebsite.com</span>
        </li>
        <li>
          <svg viewBox="0 0 24 24" aria-hidden="true"><circle cx="12" cy="12" r="10" fill="var(--sky)"/><path d="M2 12h20M12 2c3 3 3 17 0 20M12 2c-3 3-3 17 0 20" fill="none" stroke="#fff" stroke-width="1.4"/></svg>
          <span>www.mywebsite.com</span>
        </li>
      </ul>
    </div>
  </section>
</main>
</body>
</html>
```